Postcard flyer for body postive dance classes

We need an eye catching double sided A6 postcard for body positive dance classes. The business name is stepbloomjoy and already have a rough logo and some text that needs tidying up and putting together. The design needs to be simple and elegant. We are appealing to a diverse range of adult women with or without dance experience to join us in a safe, supportive and creative environment. We would like the design to use black, white and a soft green. The final design should communicate movement, contentment and wholeness. File with information attached.

Target Market(s)

Diverse range of adult women

Industry/Entity Type

Health And Wellness

Font styles to use
Other font styles liked:
• Candara or similar but open to suggestions

Colors
abd036
cadf82
eaf2ce
fffefb
fef9ed
fff3d1
ffffff

Requirements
Must have
• Logo and text provided.
Nice to have
• Sense of movement. Match to website colours and style.
Should not have
• Intimidating perfect body images

```html
<!DOCTYPE html>
<html lang="en">
<head>
<meta charset="utf-8">
<title>stepbloomjoy postcard</title>
<link rel="stylesheet" href="https://fonts.googleapis.com/css2?family=Great+Vibes&family=Crimson+Text:ital,wght@0,400;0,700;1,400&family=Lato:wght@400&display=swap">
<style>
  :root {
    --backdrop: #3b3b3b;
    --card: #ffffff;
    --ink: #111111;
    --grey: #6a6a6a;
    --green: #7fa421;
    --band: #bfd76f;
    --photo-light: #e9e9e9;
    --photo-dark: #8c8c8c;
  }
  * { margin: 0; padding: 0; box-sizing: border-box; }
  html, body { width: 848px; height: 1200px; overflow: hidden; }
  body { background: var(--backdrop); position: relative; font-family: "Crimson Text", Georgia, serif; color: var(--ink); }

  .card { position: absolute; left: 51px; width: 750px; background: var(--card); overflow: hidden; }
  .card--front { top: 54px; height: 532px; }
  .card--back { top: 614px; height: 530px; }
  .band { position: absolute; left: 0; right: 0; bottom: 0; height: 32px; background: var(--band); }

  .photo { position: absolute; }
  .photo--front-dancer { left: 13px; top: 14px; width: 268px; height: 484px;
    background: radial-gradient(ellipse at 50% 45%, var(--photo-dark) 0%, #b9b9b9 45%, var(--card) 75%); }
  .photo--back-dancer { left: 69px; top: 330px; width: 168px; height: 168px;
    background: radial-gradient(ellipse at 55% 50%, #c4c4c4 0%, var(--photo-light) 45%, var(--card) 75%); }

  .brand { position: absolute; text-align: center; transform: translateX(-50%); }
  .brand__name { display: block; font-weight: 400; color: var(--grey); letter-spacing: 0.5px; }
  .brand__tagline { display: block; font-style: italic; color: var(--ink); }
  .card--front .brand { left: 549px; top: 62px; }
  .card--front .brand__name { font-size: 38px; line-height: 1; margin-bottom: 38px; }
  .card--front .brand__tagline { font-size: 10px; }
  .card--back .brand { left: 187px; top: 42px; }
  .card--back .brand__name { font-size: 26px; line-height: 1; margin-bottom: 30px; }
  .card--back .brand__tagline { font-size: 6px; }

  .headline { position: absolute; left: 353px; width: 356px; text-align: center; font-family: "Great Vibes", cursive; line-height: 1; }
  .headline--joy { top: 206px; font-size: 42px; color: var(--green); }
  .headline--love { top: 250px; font-size: 58px; color: var(--ink); }

  .lead { position: absolute; left: 353px; width: 356px; top: 330px; text-align: center; font-weight: 700; font-size: 15.5px; line-height: 21px; }

  .invite { position: absolute; left: 353px; top: 396px; width: 356px; height: 78px; border: 1px solid var(--ink); border-radius: 10px;
    display: flex; align-items: center; justify-content: center; text-align: center; font-style: italic; font-size: 15px; line-height: 20.5px; padding: 0 8px; }

  .slogan { position: absolute; left: 24px; width: 300px; top: 138px; text-align: center; font-family: "Great Vibes", cursive; font-size: 33px; line-height: 36px; }

  .contact { position: absolute; left: 74px; width: 200px; top: 226px; text-align: center; font-family: "Lato", sans-serif; list-style: none; }
  .contact li { font-size: 14px; line-height: 23px; }
  .contact .contact__phone { font-size: 17px; }

  .stamp { position: absolute; left: 623px; top: 40px; width: 86px; height: 86px; }
  .address-lines { position: absolute; left: 455px; top: 308px; width: 266px; }
  .address-lines span { display: block; height: 2px; background: var(--ink); margin-bottom: 37px; }
</style>
</head>
<body>
  <section class="card card--front">
    <div class="photo photo--front-dancer" role="img" aria-label="Black and white photo of a smiling woman dancing in a ruffled skirt"></div>
    <div class="brand">
      <span class="brand__name">stepbloomjoy</span>
      <span class="brand__tagline">movement, contentment, wholeness</span>
    </div>
    <p class="headline headline--joy">Dance is joy</p>
    <p class="headline headline--love">Dance is love</p>
    <p class="lead">Dance is at the core of our being, a celebration of<br>movement, vitality and wholeness.</p>
    <p class="invite">If you’ve never danced before and always wanted to or you want to reignite your past love of dance, join us at stepbloomjoy to start your journey.</p>
    <div class="band"></div>
  </section>

  <section class="card card--back">
    <div class="brand">
      <span class="brand__name">stepbloomjoy</span>
      <span class="brand__tagline">movement, contentment, wholeness</span>
    </div>
    <p class="slogan">Flow with life through<br>your inner dancer.</p>
    <ul class="contact">
      <li>maya@stepbloomjoy.com.au</li>
      <li class="contact__phone">CALL US: 0400718264</li>
      <li>www.stepbloomjoy.com.au</li>
      <li class="contact__phone">Leura/Wentworth</li>
    </ul>
    <div class="photo photo--back-dancer" role="img" aria-label="Soft black and white photo of a ballet dancer in arabesque"></div>
    <svg class="stamp" viewBox="0 0 86 86" aria-hidden="true">
      <path d="M4 4 Q8 1 12 4 Q16 1 20 4 Q24 1 28 4 Q32 1 36 4 Q40 1 44 4 Q48 1 52 4 Q56 1 60 4 Q64 1 68 4 Q72 1 76 4 Q80 1 82 4
               Q85 8 82 12 Q85 16 82 20 Q85 24 82 28 Q85 32 82 36 Q85 40 82 44 Q85 48 82 52 Q85 56 82 60 Q85 64 82 68 Q85 72 82 76 Q85 80 82 82
               Q78 85 74 82 Q70 85 66 82 Q62 85 58 82 Q54 85 50 82 Q46 85 42 82 Q38 85 34 82 Q30 85 26 82 Q22 85 18 82 Q14 85 10 82 Q6 85 4 82
               Q1 78 4 74 Q1 70 4 66 Q1 62 4 58 Q1 54 4 50 Q1 46 4 42 Q1 38 4 34 Q1 30 4 26 Q1 22 4 18 Q1 14 4 10 Q1 6 4 4 Z"
            fill="none" stroke="#555" stroke-width="0.8"/>
    </svg>
    <div class="address-lines"><span></span><span></span><span></span><span></span></div>
    <div class="band"></div>
  </section>
</body>
</html>
```